Mental Health Awareness License Plates

Below is the sample format I will need. That of a plain license plate w/o frame
*refer to image with name Licence wo Frame*
Delete Frame
Replace QR Code with “MO”
Replace 2025 sticker with “ YR
Use License Plate font (attached)
On Ribbon, keep the green background
The California front leg, needs to be gradated like a sunset and retain shape of CA
Palm trees sharpened
I need the files in a format that can be used on a website, printed or made into a poster.
One file that reads SAMPLE, one version that reads “NEWPLA8”d
The finished product should look like a license plate as shown in the example
*refer to image name finished product*
I want to clarify what we are looking for. The license plate design has been approved by the state, but we need a high res version of it in multiple file formats. The most important change we are looking for is to the ribbon. The palm trees against the sunset are fuzzy, we need those placed in front of an sunset on the front leg of the ribbon. The rear leg needs to remain green (mental health color). I hope this help clarify our design need.

```html
<!DOCTYPE html>
<html lang="en">
<head>
<meta charset="utf-8">
<title>Mental Health Awareness Plate</title>
<link rel="stylesheet" href="https://fonts.googleapis.com/css2?family=Oswald:wght@400;600&family=Sniglet:wght@800&display=swap">
<style>
  :root {
    --page-bg: #ffffff;
    --plate-rim: #a6f3e2;
    --plate-face: #b0f8ea;
    --ink: #224a6a;
    --label: #76dcc4;
    --ribbon-green: #24a31f;
    --sunset-top: #f28a00;
    --sunset-mid: #f4b20c;
    --sunset-low: #fdf53a;
  }
  html, body {
    margin: 0;
    width: 1200px;
    height: 761px;
    overflow: hidden;
    background: var(--page-bg);
  }
  .plate-canvas {
    position: relative;
    width: 1200px;
    height: 761px;
  }
  .plate-art { position: absolute; inset: 0; }
  .plate-rim { fill: var(--plate-rim); }
  .plate-face { fill: var(--plate-face); }
  .bolt { fill: var(--ink); }
  .divider { stroke: var(--label); stroke-width: 1.5; }
  .sticker-label {
    font-family: "Oswald", sans-serif;
    font-weight: 400;
    font-size: 54px;
    fill: var(--label);
  }
  .state-name {
    font-family: "Sniglet", sans-serif;
    font-weight: 800;
    font-size: 122px;
    fill: var(--ink);
  }
  .plate-number {
    font-family: "Oswald", sans-serif;
    font-weight: 600;
    font-size: 236px;
    fill: var(--ink);
  }
  .awareness-ribbon {
    position: absolute;
    left: 223px;
    top: 351px;
    width: 138px;
    height: 239px;
    border-radius: 48px 48px 10px 10px;
    background: linear-gradient(100deg, var(--ribbon-green) 0%, var(--ribbon-green) 30%, var(--sunset-top) 42%, var(--sunset-mid) 75%, var(--sunset-low) 100%);
  }
</style>
</head>
<body>
<main class="plate-canvas">
  <svg class="plate-art" width="1200" height="761" viewBox="0 0 1200 761" xmlns="http://www.w3.org/2000/svg">
    <rect class="plate-rim" x="94" y="102" width="991" height="564" rx="48"/>
    <rect class="plate-face" x="118" y="125" width="944" height="518" rx="26"/>

    <circle class="bolt" cx="175" cy="187" r="20"/>
    <circle class="bolt" cx="1004" cy="187" r="20"/>
    <circle class="bolt" cx="175" cy="580" r="20"/>
    <circle class="bolt" cx="1004" cy="580" r="20"/>

    <text class="sticker-label" x="314" y="265" textLength="113" lengthAdjust="spacingAndGlyphs">MONTH</text>
    <line class="divider" x1="473" y1="185" x2="473" y2="328"/>
    <text class="sticker-label" x="535" y="265" textLength="89" lengthAdjust="spacingAndGlyphs">YEAR</text>

    <text class="state-name" x="777" y="285" textLength="216" lengthAdjust="spacingAndGlyphs">CAL</text>

    <text class="plate-number" x="440" y="556" textLength="502" lengthAdjust="spacingAndGlyphs">NEWPL</text>
  </svg>
  <div class="awareness-ribbon" role="img" aria-label="Green mental health awareness ribbon whose front leg is a California-shaped sunset with palm tree silhouettes"></div>
</main>
</body>
</html>
```